Exclusive beauty salon needs a price list or services booklet

I need a new very attractive flyer for my beauty salon, containing information on the different services and their prices.
In attachment you can find a pdf of the "old" one, but I'd love to have a beautifully designed new one!
I'd love to have a booklet in format 148 x 148 mm, or in US format, containing 12 or 16 pages, but if you can offer other nice looking designs they are welcome!
The services that need to come in the booklet with their prices can all be found on my website: www.atelierkova.be, starting with
Gelaatsverzorging
Wimperverlenging
Suikerontharing
Wimperlifting
Permanente Make Up
Airbrush Tanning

Target Market(s)

woman from 20 to 89 years old

Industry/Entity Type

Beauty Salon

Font styles to use
Sans Serif

Colors

Designer to choose colors to be used in the design.

Requirements
Must have
• a classy nice look, it must contain details about the services from my beauty salon and their prices, and nice pictures.
• The Names, prices and explanations of the services can easily be found on my website: www.atelierkova.be
Nice to have
• In attachment you can find the "old" price list in pdf, what I need now is a "new booklet" with the new logo and updated services price list.
• I need a very nice and attractive looking booklet, classy chique, Paris chique, looking very expensive.
Should not have
• Not too much colors, not too curly, but still feminine

```html
<!DOCTYPE html>
<html lang="nl">
<head>
<meta charset="utf-8">
<title>Testimonials – Atelier Kova</title>
<link rel="stylesheet" href="https://fonts.googleapis.com/css2?family=Open+Sans:wght@300;400;600;700&display=swap">
<style>
  :root {
    --slate: #6d6e71;
    --ink: #000000;
    --paper: #ffffff;
    --bg-light: #eeeeed;
    --bg-shade: #d9d9d7;
    --text-dark: #3a3a3c;
  }
  html, body {
    margin: 0;
    padding: 0;
    width: 1200px;
    height: 1200px;
    overflow: hidden;
    background: var(--paper);
  }
  .page {
    display: block;
    width: 1200px;
    height: 1200px;
  }
  .title {
    font-family: "Open Sans", sans-serif;
    font-weight: 400;
    font-size: 70px;
    fill: var(--paper);
  }
  .quote {
    font-family: "Open Sans", sans-serif;
    font-weight: 300;
    font-size: 28px;
    fill: var(--paper);
  }
  .author {
    font-family: "Open Sans", sans-serif;
    font-weight: 400;
    font-size: 37px;
    fill: var(--text-dark);
  }
  .contact {
    font-family: "Open Sans", sans-serif;
    font-weight: 400;
    font-size: 26px;
    fill: var(--paper);
  }
  .web {
    font-family: "Open Sans", sans-serif;
    font-weight: 700;
    font-size: 36px;
    letter-spacing: 0.36em;
    fill: var(--paper);
  }
</style>
</head>
<body>
<svg class="page" viewBox="0 0 1200 1200" xmlns="http://www.w3.org/2000/svg">
  <defs>
    <linearGradient id="palmTone" x1="0" y1="0" x2="1" y2="1">
      <stop offset="0" stop-color="var(--bg-light)"/>
      <stop offset="0.5" stop-color="var(--bg-shade)"/>
      <stop offset="1" stop-color="var(--bg-light)"/>
    </linearGradient>
    <clipPath id="testimonialDisc">
      <circle cx="591" cy="0" r="600"/>
    </clipPath>
  </defs>

  <!-- background photo area -->
  <rect class="backdrop" x="0" y="0" width="1200" height="1080" fill="url(#palmTone)" role="img" aria-label="Faded photo of palm trees over a soft chevron pattern"/>

  <!-- testimonial disc -->
  <g class="testimonial-disc">
    <circle cx="600" cy="26" r="600" fill="var(--ink)"/>
    <circle cx="591" cy="0" r="600" fill="var(--slate)"/>
    <g clip-path="url(#testimonialDisc)">
      <rect class="name-band" x="0" y="256" width="1200" height="53" fill="var(--paper)"/>
      <rect class="name-band" x="0" y="388" width="1200" height="50" fill="var(--paper)"/>
    </g>

    <text class="title" x="597" y="120" text-anchor="middle">TESTIMONIALS</text>

    <text class="quote" x="597" y="171" text-anchor="middle">“IK BEN AL JAREN KLANT BIJ NADIA EN WORDT NOG STEEDS MET</text>
    <text class="quote" x="597" y="208" text-anchor="middle">HETZELFDE ENTHOUSIASME ONTVANGEN. IK KOM ALTIJD HELEMAAL ZEN</text>
    <text class="quote" x="597" y="244" text-anchor="middle">BUITEN!"</text>
    <text class="author" x="597" y="296" text-anchor="middle">SOFIE / ZELFSTANDIGE / EEKLO</text>

    <text class="quote" x="597" y="375" text-anchor="middle">“SUPER BLIJ MET MIJN WIMPERTJES!"</text>
    <text class="author" x="597" y="426" text-anchor="middle">LOTTE  / DIRECTIEASSISTENTE / ADEGEM</text>
  </g>

  <!-- contact dome -->
  <g class="contact-dome">
    <circle cx="597" cy="1121" r="315" fill="var(--slate)"/>
    <circle cx="600" cy="1124" r="302" fill="var(--ink)"/>
    <text class="contact" x="597" y="926" text-anchor="middle">Tel: 0470 31 56 19</text>
    <text class="contact" x="597" y="963" text-anchor="middle">Kerkstraat 41 (2e verdieping</text>
    <text class="contact" x="597" y="1001" text-anchor="middle">Lindegebouw) 9900 EEKLO</text>
    <text class="contact" x="597" y="1038" text-anchor="middle">nadia@atelierkova.be</text>
  </g>

  <!-- footer band -->
  <rect class="footer-band" x="0" y="1080" width="1200" height="120" fill="var(--slate)"/>
  <text class="web" x="610" y="1137" text-anchor="middle">www.atelierkova.be</text>
</svg>
</body>
</html>
```